Poem Handwritten by Veteran while in the jungle of Vietnam

My parents are celebrating their 50th wedding anniversary this year. I wanted to give them a very memorable gift. On my parents 2nd anniversary, my father was stationed in Vietnam. On that night he was in the jungle waiting till morning and wrote a poem to my mother using his pant leg as paper. I would like this poem to typographically designed to be framed and hung on the wall.

I have attached a picture of the poem below. It will need to be 11x14 when printed for framing. It would be great if there was background or artwork to make it more visually interesting, perhaps in a watercolor. My parents have a transitional style. I have attached some possible color schemes as well. Cool greens, blue, neutral grays, with hints of berries or highlights of yellow. These are just a guide, I would be open to your interpretations.

Thank you for your help. This will hopefully be a gift they will truly treasure as much as the poem itself.

Target Market(s)

My parents who are excited to be celebrating their 50th wedding anniversary. It should have a transitional, mature style.

Font styles to use
Serif
Script

Requirements
Must have
• The poem, typographically designed. There can be a mix of fonts, but legibility is critically important.
• Now that some designs have come through I wanted to give some more guidance of what I'm looking for. I want something that feels sophisticated and artistic.
Nice to have
• A background or art work, using the color schemes attached as a guide. I am really liking the designs that have a full color landscape artwork in the background. The fonts should be elegant and formal. I really like the romantic, muted colors. I had trouble finding similar projects online in the style I wanted until I cam across wedding invites. Those seem to be the most applicable. I've added pictures of some so you can get a sense of what I'm looking for. I am really liking the jungle foliage, starry skies or sunrises.
Should not have
• Cartoon caricatures, fonts that are too illegible when printed. I'm not liking anything whimsical. I don't like the very bright colors for this project.

```html
<!DOCTYPE html>
<html lang="en">
<head>
<meta charset="utf-8">
<title>Happy Anniversary Darling – Anniversary Poem</title>
<link href="https://fonts.googleapis.com/css2?family=Alex+Brush&family=Dancing+Script:wght@500&family=Parisienne&display=swap" rel="stylesheet">
<style>
  :root {
    --page-bg: #f4f2ee;
    --sky-top: #bfe2f3;
    --sky-mid: #e6f0dc;
    --haze: #eef2cf;
    --meadow: #9ccb72;
    --meadow-deep: #6fae55;
    --title-olive: #6a6a2c;
    --title-shadow: #2f3a22;
    --ink: #2b3a4e;
  }
  * { margin: 0; padding: 0; box-sizing: border-box; }
  html, body { width: 1200px; height: 1200px; overflow: hidden; background: var(--page-bg); }
  .poster {
    position: absolute; left: 161px; top: 20px;
    width: 878px; height: 1160px; overflow: hidden;
  }
  .poster-art { position: absolute; inset: 0; width: 100%; height: 100%; }
  .title {
    position: absolute; left: 0; right: 0; top: 22px;
    text-align: center;
    font-family: "Alex Brush", cursive;
    font-size: 68px; line-height: 62px;
    color: var(--title-olive);
    text-shadow: 2px 3px 0 var(--title-shadow), 0 0 2px rgba(255,255,255,.6);
  }
  .dateline {
    position: absolute; left: 156px; top: 205px;
    font-family: "Dancing Script", cursive;
    color: var(--ink); font-size: 38px; line-height: 48px;
  }
  .poem-column {
    position: absolute; width: 360px; text-align: center;
    font-family: "Parisienne", cursive;
    color: var(--ink); font-size: 18px; line-height: 23.5px;
  }
  .poem-column.left { left: 103px; top: 340px; }
  .poem-column.right { left: 438px; top: 450px; }
  .stanza { margin-bottom: 23.5px; }
  .note {
    position: absolute; left: 40px; right: 40px; top: 1072px;
    text-align: center;
    font-family: "Parisienne", cursive;
    color: var(--ink); font-size: 16px; line-height: 23px;
  }
</style>
</head>
<body>
<main class="poster">
  <svg class="poster-art" viewBox="0 0 878 1160" preserveAspectRatio="none" role="img" aria-label="Soft watercolour landscape: helicopter over a jungle tree line, a soldier resting in a green meadow">
    <defs>
      <linearGradient id="landscape" x1="0" y1="0" x2="0" y2="1">
        <stop offset="0" stop-color="var(--sky-top)"/>
        <stop offset="0.3" stop-color="var(--sky-mid)"/>
        <stop offset="0.55" stop-color="var(--haze)"/>
        <stop offset="0.7" stop-color="var(--meadow)"/>
        <stop offset="1" stop-color="var(--meadow-deep)"/>
      </linearGradient>
    </defs>
    <rect width="878" height="1160" fill="url(#landscape)"/>
  </svg>

  <h1 class="title">Happy Anniversary<br>Darling.</h1>

  <p class="dateline">20 July 1970, Monday LZ Professional<br>Walter’s Anniversary Poem</p>

  <section class="poem-column left">
    <p class="stanza">Life’s journey began with a challenge,<br>It was heralded far and near.<br>The road led on forever,<br>Its completion was known to be dear.</p>
    <p class="stanza">From the garden of light it proceeded,<br>To the valley of shadows it led.<br>Thorns and thistles adorned it,<br>Past abyss and crevice it sped.</p>
    <p class="stanza">The brave surged forward with courage,<br>The wise undaunted pressed on,<br>The mighty held high their banner,<br>We all awaited the dawn.</p>
    <p class="stanza">Though the pitfalls and hazards were many,<br>The pathway was clearly in view.<br>Straight and sure it glided,<br>Its course we knew to be true.</p>
    <p class="stanza">I knew you, Sweetheart, beforehand,<br>So precious and sweet were you.<br>Our moments of bliss were priceless,<br>Each day brought us joy anew.</p>
    <p class="stanza">The call to progression beckoned,<br>At last I would have my chance<br>To clasp you to me forever,<br>And seal our divine romance.</p>
  </section>

  <section class="poem-column right">
    <p class="stanza">I eagerly started the journey,<br>Though with sorrow, I left you behind.<br>With courage and faith I continued,<br>For I knew, that you later I’d find.</p>
    <p class="stanza">I diligently searched for you, Darling,<br>The roadway was both bleak and fair.<br>Though the years grew long in number,<br>I did not give up in despair.</p>
    <p class="stanza">At last in the distance I saw you,<br>So beautiful lovely and sweet.<br>Your attention I struggled to capture,<br>Your love I wrested to meet.</p>
    <p class="stanza">What rapture was mine in fulfillment,<br>As now together we stand,<br>To cherish and love each other,<br>While our plans and dreams expand.</p>
    <p class="stanza">I love you, Darling, forever,<br>My life you have made replete.<br>Our eternal mansion beckons,<br>Your love has made it complete.</p>
  </section>

  <p class="note">This poem was written during the dark of night while on guard duty at LZ Professional in Viet Nam. I was at the time a 2nd Lieutenant in the Infantry. The date was July 1970, our second anniversary. The original was penciled onto my fatigue uniform, arranging only the key rhyming words without light to see.</p>
</main>
</body>
</html>
```